smart IT for growing teams

Let’s design a business card that will be as simple and bold at the same time. Name, email address, website & phone number.

Target Market(s)

Small to Medium Size Business

Industry/Entity Type

It Professional

Contact Information for Business Card

Name, email, website, phone numbers

Font styles to use
Sans Serif

Colors
ec1f27
f04a50
dddddd
919191
000000
ffffff

Requirements
Must have
• Clean simple look using my existing logo. I just need to the basic contact information on this card.
Nice to have
• Im considering the square size card versus the standard size business card.
Should not have
• No Mailing Address, no list of services.

```html
<!DOCTYPE html>
<html lang="en">
<head>
<meta charset="utf-8">
<title>Kestrel Systems — Square Business Card</title>
<link rel="stylesheet" href="https://fonts.googleapis.com/css2?family=Open+Sans:wght@400;600;700&display=swap">
<style>
  :root {
    --red: #ec1f27;
    --red-soft: #f04a50;
    --light-grey: #dddddd;
    --mid-grey: #919191;
    --black: #000000;
    --white: #ffffff;
    --stage: #7d7d7d;
  }
  * { box-sizing: border-box; margin: 0; padding: 0; }
  html, body {
    width: 1200px;
    height: 904px;
    overflow: hidden;
    background: var(--stage);
    font-family: "Open Sans", sans-serif;
  }
  .sheet {
    width: 1200px;
    height: 904px;
    display: flex;
    align-items: center;
    justify-content: center;
    gap: 80px;
  }
  .card {
    position: relative;
    width: 440px;
    height: 440px;
    background: linear-gradient(160deg, var(--white) 0%, #ececec 100%);
    overflow: hidden;
    box-shadow: 0 10px 30px rgba(0,0,0,0.35);
  }

  /* Front: contact side */
  .card-front .backdrop-disc {
    position: absolute;
    left: 70px;
    top: 90px;
    width: 300px;
    height: 300px;
    border-radius: 50%;
    border: 28px solid var(--light-grey);
    opacity: 0.75;
  }
  .contact-block {
    position: absolute;
    inset: 0;
    display: flex;
    flex-direction: column;
    align-items: center;
    padding-top: 112px;
    text-align: center;
  }
  .person-name {
    color: var(--red);
    font-weight: 700;
    font-size: 22px;
    line-height: 1.1;
  }
  .person-role {
    color: var(--black);
    font-size: 14px;
    margin-top: 2px;
  }
  .icon-row {
    display: flex;
    gap: 38px;
    margin-top: 26px;
  }
  .icon-row svg { width: 30px; height: 30px; }
  .contact-lines {
    margin-top: 28px;
    color: var(--black);
    font-size: 16px;
    line-height: 1.45;
  }

  /* Back: brand side */
  .brand {
    position: absolute;
    left: 0;
    right: 0;
    top: 160px;
    display: flex;
    flex-direction: column;
    align-items: center;
  }
  .brand-name {
    font-weight: 400;
    font-size: 38px;
    line-height: 1.1;
    color: var(--black);
  }
  .brand-tagline {
    font-size: 14px;
    color: var(--mid-grey);
    margin-top: 6px;
    letter-spacing: 0.5px;
  }
  .brand-band {
    position: absolute;
    left: 0;
    right: 0;
    height: 32px;
    background: var(--black);
  }
  .brand-band.top { top: 300px; }
  .brand-band.bottom { top: 392px; }
  .brand-dot {
    position: absolute;
    left: 50%;
    top: 362px;
    width: 40px;
    height: 40px;
    margin: -20px 0 0 -20px;
    border-radius: 50%;
    background: var(--red);
  }
</style>
</head>
<body>
<main class="sheet">
  <section class="card card-front" aria-label="Contact side">
    <div class="backdrop-disc"></div>
    <div class="contact-block">
      <h1 class="person-name">John Smith</h1>
      <p class="person-role">Manager</p>
      <div class="icon-row">
        <svg viewBox="0 0 30 30" aria-label="Phone">
          <circle cx="15" cy="15" r="13" fill="var(--white)" stroke="var(--red)" stroke-width="1.6"/>
          <path d="M10.5 9.5c1-1 2-1 2.5 0l1 2c.3.6 0 1.1-.5 1.5l-.6.5c.6 1.5 1.7 2.6 3.2 3.2l.5-.6c.4-.5.9-.8 1.5-.5l2 1c1 .5 1 1.5 0 2.5-1.5 1.5-4 1-6.6-1.6s-3.1-5.1-1.6-6.6z" fill="var(--red)"/>
        </svg>
        <svg viewBox="0 0 30 30" aria-label="Email">
          <circle cx="15" cy="15" r="13" fill="var(--white)" stroke="var(--red)" stroke-width="1.6"/>
          <rect x="8.5" y="10.5" width="13" height="9" rx="1" fill="var(--red)"/>
          <path d="M8.8 11l6.2 4.5 6.2-4.5" fill="none" stroke="var(--white)" stroke-width="1.2"/>
        </svg>
        <svg viewBox="0 0 30 30" aria-label="Website">
          <circle cx="15" cy="15" r="13" fill="var(--white)" stroke="var(--red)" stroke-width="1.6"/>
          <circle cx="15" cy="15" r="6.5" fill="none" stroke="var(--red)" stroke-width="1.4"/>
          <ellipse cx="15" cy="15" rx="2.8" ry="6.5" fill="none" stroke="var(--red)" stroke-width="1.2"/>
          <path d="M8.5 15h13" stroke="var(--red)" stroke-width="1.2"/>
        </svg>
      </div>
      <div class="contact-lines">
        <p>+999 9999 9999</p>
        <p>info@mywebsite.com</p>
        <p>www.mywebsite.com</p>
      </div>
    </div>
  </section>

  <section class="card card-back" aria-label="Brand side">
    <div class="brand">
      <p class="brand-name">Kestrel Systems</p>
      <p class="brand-tagline">smart IT for growing teams</p>
    </div>
    <div class="brand-band top"></div>
    <div class="brand-dot"></div>
    <div class="brand-band bottom"></div>
  </section>
</main>
</body>
</html>
```